Dynamic Business Card for Sports Supplements Company

Hi! I'm looking for an awesome business card to match my existing sports supplement company. I have uploaded my current company logo and screenshot of the front page of my website.

I would like to have something dynamic and interesting and utilize the colors in the website - the reds and purples

The business card should be double sided and focus on a unique eye-catching design on the back and include all the relevant company info.

Most importantly, it should say somewhere: "Sign up on our website for a coupon code."

Target Market(s)

Mostly for women gym goers but it shouldn't be too feminine. It should be in keeping with the website design. It should flow and clearly be connected to it

Industry/Entity Type

Business

Contact Information for Business Card

Lorena K. Vasquez
CEO
LVasquez@Fortivanco.example
www.fortivanco.example
614.275.3081
P.O. Box 48317
Calder Falls, Westvale 22417

Sign up on our website for a coupon code

Font styles to use
Serif
Sans Serif
Other font styles liked:
• Novecento font family and "Fortivan" is in AR Destine font

Requirements
Must have
• One side should be a bold Fortivan logo design. Even just the symbol itself may be o.k. (see attached file)

```html
<!DOCTYPE html>
<html lang="en">
<head>
<meta charset="utf-8">
<title>Fortivan Business Card</title>
<link rel="stylesheet" href="https://fonts.googleapis.com/css2?family=Roboto:wght@400;500;700&display=swap">
<style>
  :root {
    --backdrop: #8f8f8f;
    --card: #111111;
    --red: #e62228;
    --white: #ffffff;
    --text-light: #f2f2f2;
  }
  html, body {
    margin: 0;
    padding: 0;
    width: 1200px;
    height: 1200px;
    overflow: hidden;
    background: var(--backdrop);
    font-family: "Roboto", Arial, sans-serif;
  }
  .card {
    position: absolute;
    background: var(--card);
    box-shadow: 6px 8px 14px rgba(0,0,0,0.45);
    overflow: hidden;
  }
  .card--front { left: 146px; top: 47px; width: 908px; height: 523px; }
  .card--back  { left: 143px; top: 629px; width: 914px; height: 524px; }

  .brand {
    position: absolute;
    display: flex;
    flex-direction: column;
    align-items: center;
    color: var(--white);
  }
  .brand__mark { background: var(--red); }
  .brand__name {
    font-weight: 700;
    letter-spacing: 0.04em;
    line-height: 1;
    text-transform: uppercase;
  }
  .brand__tagline {
    font-weight: 500;
    letter-spacing: 0.16em;
    line-height: 1;
    white-space: nowrap;
  }

  .card--front .brand { left: 70px; top: 158px; width: 340px; }
  .card--front .brand__mark { width: 110px; height: 110px; margin-bottom: 36px; }
  .card--front .brand__name { font-size: 50px; }
  .card--front .brand__tagline { font-size: 15px; margin-top: 8px; }

  .divider {
    position: absolute;
    left: 453px;
    top: 143px;
    width: 3px;
    height: 240px;
    background: var(--red);
  }

  .contact {
    position: absolute;
    left: 502px;
    top: 128px;
    color: var(--text-light);
  }
  .contact__name {
    margin: 0;
    color: var(--red);
    font-size: 36px;
    font-weight: 500;
    line-height: 1.1;
  }
  .contact__role {
    margin: 2px 0 0;
    font-size: 22px;
    line-height: 1.1;
  }
  .contact__address {
    margin: 22px 0 0;
    font-style: normal;
    font-size: 23px;
    line-height: 30px;
  }
  .contact__list {
    list-style: none;
    margin: 18px 0 0;
    padding: 0;
    font-size: 23px;
    line-height: 29px;
  }
  .contact__list li {
    display: flex;
    align-items: center;
    gap: 10px;
  }
  .contact__icon {
    width: 20px;
    height: 20px;
    flex: none;
    fill: var(--red);
  }

  .band {
    position: absolute;
    left: 0;
    right: 0;
    bottom: 0;
    background: var(--red);
    color: var(--white);
    display: flex;
    align-items: center;
    justify-content: center;
  }
  .card--front .band { height: 23px; }
  .card--back .band { height: 56px; font-size: 24px; font-weight: 400; }

  .card--back .brand { left: 0; right: 0; top: 128px; }
  .card--back .brand__mark { width: 160px; height: 160px; margin-bottom: 42px; }
  .card--back .brand__name { font-size: 66px; }
  .card--back .brand__tagline { font-size: 19px; margin-top: 10px; }
</style>
</head>
<body>

<section class="card card--front" aria-label="Card front">
  <div class="brand">
    <div class="brand__mark"></div>
    <div class="brand__name">Fortivan</div>
    <div class="brand__tagline">your training companion</div>
  </div>

  <div class="divider"></div>

  <div class="contact">
    <h1 class="contact__name">Lorena K. Vasquez</h1>
    <p class="contact__role">CEO</p>
    <address class="contact__address">P.O. Box 48317<br>Calder Falls, Westvale 22417</address>
    <ul class="contact__list">
      <li>
        <svg class="contact__icon" viewBox="0 0 24 24" aria-hidden="true"><path d="M6.6 10.8a15.1 15.1 0 0 0 6.6 6.6l2.2-2.2c.3-.3.7-.4 1-.2 1.1.4 2.3.6 3.6.6.6 0 1 .4 1 1V20c0 .6-.4 1-1 1A17 17 0 0 1 3 4c0-.6.4-1 1-1h3.5c.6 0 1 .4 1 1 0 1.3.2 2.5.6 3.6.1.3 0 .7-.2 1z"/></svg>
        <span>614.275.3081</span>
      </li>
      <li>
        <svg class="contact__icon" viewBox="0 0 24 24" aria-hidden="true"><path d="M2 5h20v14H2z M4 7v.4l8 5.4 8-5.4V7z" fill-rule="evenodd"/></svg>
        <span>LVasquez@Fortivanco.example</span>
      </li>
      <li>
        <svg class="contact__icon" viewBox="0 0 24 24" aria-hidden="true"><path d="M12 2a10 10 0 1 0 0 20 10 10 0 0 0 0-20zm0 2c.9 0 2.2 2 2.7 5H9.3C9.8 6 11.1 4 12 4zM4.3 11h3a17 17 0 0 0 0 2h-3a8 8 0 0 1 0-2zm5 0h5.4a15 15 0 0 1 0 2H9.3a15 15 0 0 1 0-2zm7.4 0h3a8 8 0 0 1 0 2h-3a17 17 0 0 0 0-2zM9.3 15h5.4c-.5 3-1.8 5-2.7 5s-2.2-2-2.7-5zm-4.2 0h2.2c.2 1.4.6 2.6 1.1 3.6A8 8 0 0 1 5.1 15zm11.6 0h2.2a8 8 0 0 1-3.300 3.600c.5-1 .9-2.200 1.100-3.600zM5.1 9a8 8 0 0 1 3.3-3.6c-.5 1-.9 2.2-1.1 3.6zm11.6 0c-.2-1.4-.6-2.6-1.1-3.6A8 8 0 0 1 18.9 9z"/></svg>
        <span>www.fortivanco.example</span>
      </li>
    </ul>
  </div>

  <div class="band"></div>
</section>

<section class="card card--back" aria-label="Card back">
  <div class="brand">
    <div class="brand__mark"></div>
    <div class="brand__name">Fortivan</div>
    <div class="brand__tagline">your training companion</div>
  </div>

  <div class="band">Sign up on our website for a coupon code</div>
</section>

</body>
</html>
```